Virtual Personal Training Flyer Design

We are a virtual personal training website, acting as the intermediary between the customer and the personal trainer. The customer can choose their personal trainer based on specialty and then subscribe and have access to their videos, training nutritional advice and live sessions.
We have sent over an orange and blue background for inspiration of the theme and also our three logos. Brightpeak Fitness is the company and BrightpeakLDX is the product and the F is our standard logo.
We want our social media links on the flyer which are Twitter: @BrightpeakLDX and Facebook: BrightpeakLDX. We also want our e-mail address which is brightpeakldx@quillmail.net and telephone number which is 07518269352.

We also want to put the key benefits for consumers onto the flyers, which are wide variety of personal trainers to choose from and tailored to you, have constant access to videos etc, save time travelling to the gym, saving effort - more convenient, cheaper than personal training in the gym - saving money, gain from trainer's knowledge - more informed about workout and what exercises you are doing etc. We would like to add rhetorical questions such as Want a personal trainer but can't afford one? or Want to have a structured training program but haven't got the time or access to a gym?
We also want our slogan on there which is LDX, become the you, you've always wanted to be.

Target Market(s)

women aged between 18 and 35

Industry/Entity Type

Personal Trainer

Requirements
Should not have
• don't want old fonts or clash colours and shouldn't be cartooney.

```html
<!DOCTYPE html>
<html lang="en">
<head>
<meta charset="utf-8">
<title>Brightpeak Fitness – Virtual Personal Training Flyer</title>
<link rel="stylesheet" href="https://fonts.googleapis.com/css2?family=Barlow+Condensed:wght@300;400;500&display=swap">
<style>
  :root {
    --stage: #5b5e64;
    --paper: #ffffff;
    --paper-shade: #e6e6e8;
    --navy: #1f4f8f;
    --band: #2a86c3;
    --orange: #f07d1c;
    --white: #ffffff;
  }
  * { margin: 0; padding: 0; box-sizing: border-box; }
  html, body { width: 1200px; height: 1000px; overflow: hidden; }
  body {
    background: var(--stage);
    font-family: "Barlow Condensed", "Arial Narrow", sans-serif;
    position: relative;
  }
  .flyer {
    position: absolute;
    left: 271px; top: 32px;
    width: 658px; height: 923px;
    background: radial-gradient(ellipse 70% 45% at 50% 38%, var(--paper) 40%, var(--paper-shade) 100%);
    overflow: hidden;
  }
  .device-showcase {
    position: absolute;
    left: 139px; top: 183px;
    width: 460px; height: 330px;
    border-radius: 8px;
    background: linear-gradient(160deg, #e9ecf1 0%, #c9d3e2 55%, #dfe3ea 100%);
  }
  .headline {
    position: absolute;
    left: 0; right: 0; top: 566px;
    text-align: center;
    color: var(--navy);
  }
  .headline-kicker {
    display: block;
    font-weight: 300;
    font-size: 34px;
    line-height: 34px;
    letter-spacing: 0.5px;
  }
  .headline-main {
    display: block;
    font-weight: 500;
    font-size: 60px;
    line-height: 60px;
    letter-spacing: -0.5px;
  }
  .benefit-band {
    position: absolute;
    left: 0; right: 0; top: 668px;
    height: 53px;
    background: var(--band);
    color: var(--white);
    text-align: center;
    box-shadow: 0 -8px 14px rgba(0,0,0,0.08), 0 8px 14px rgba(0,0,0,0.08);
  }
  .benefit-intro {
    display: block;
    font-weight: 300;
    font-size: 22px;
    line-height: 24px;
    padding-top: 2px;
  }
  .benefit-list {
    display: block;
    font-weight: 400;
    font-size: 22px;
    line-height: 24px;
    letter-spacing: 0.3px;
  }
  .brand-mark {
    position: absolute;
    left: 0; right: 0; top: 778px;
    display: flex;
    justify-content: center;
    align-items: center;
    gap: 14px;
  }
  .brand-name {
    font-weight: 500;
    font-size: 52px;
    line-height: 52px;
    color: var(--orange);
  }
  .brand-square {
    width: 34px; height: 34px;
    background: var(--navy);
  }
  .contact-row {
    position: absolute;
    left: 60px; right: 60px; top: 868px;
    display: flex;
    justify-content: space-between;
    color: var(--navy);
    font-weight: 400;
    font-size: 17px;
    line-height: 20px;
  }
  .contact-item { display: flex; align-items: center; gap: 5px; }
  .contact-item svg { fill: var(--navy); flex: none; }
  .social-dot {
    width: 12px; height: 12px; border-radius: 50%;
    background: var(--navy);
    flex: none;
  }
</style>
</head>
<body>
  <main class="flyer">
    <div class="device-showcase" role="img" aria-label="Desktop monitor, tablet and phone showing the BrightpeakLDX website with the line 'Connecting you to the right personal trainer' and silhouettes of people exercising"></div>

    <h1 class="headline">
      <span class="headline-kicker">VIRTUAL</span>
      <span class="headline-main">PERSONAL TRAINING WEBSITE</span>
    </h1>

    <div class="benefit-band">
      <span class="benefit-intro">Choose your trainer and get instant access to</span>
      <span class="benefit-list">VIDEOS &bull; TRAINING &bull; NUTRITIONAL ADVICE &bull; LIVE SESSIONS</span>
    </div>

    <div class="brand-mark">
      <span class="brand-name">Brightpeak Fitness</span>
      <span class="brand-square"></span>
    </div>

    <footer class="contact-row">
      <span class="contact-item">
        <svg width="12" height="16" viewBox="0 0 12 16"><path d="M3 1 L5 1 L6 5 L4.5 6.2 C5 8.5 6 10 7.5 11 L9 10 L11.5 12 L10.5 14.5 C6 15 1.5 9 2 3 Z"/></svg>
        0 (751) 826-9352
      </span>
      <span class="contact-item">
        <svg width="20" height="14" viewBox="0 0 20 14"><rect x="0" y="0" width="20" height="14"/><path d="M1 1 L10 8 L19 1" fill="none" stroke="#fff" stroke-width="1.5"/></svg>
        brightpeakldx@quillmail.net
      </span>
      <span class="contact-item"><span class="social-dot"></span>@BrightpeakLDX</span>
      <span class="contact-item"><span class="social-dot"></span>BrightpeakLDX</span>
    </footer>
  </main>
</body>
</html>
```